【 概要 】 都内で7年目のイタリアンレストランです。 コロナ渦でテイクアウト営業に勤しんでおります。 今までスタッフが書いたチラシで頑張ってましたが、メニュー改訂もあり是非プロのお力添えを頂きたく募集致しました。 素敵なデザインを楽しみにしております。 【 依頼内容 】 ・サイズ:A4 片面 ・ページ数:1ページ ・素材の用意(画像・文章等):添付ファイル1枚目がメニューです ・デザイン内容:添付ファイル2枚目がイメージです。料理や人物を参考にお願いします 【 デザインイメージ 】 ・ターゲット層:都心在住の30〜50代男女 ・雰囲気:ナチュラルでおしゃれな雰囲気 ・参考デザイン: お店のイメージ(URL参考)添付ファイル2枚目参照 【 契約金額(税抜) 】 2万円 ※契約金額(税込)からシステム利用料を差し引いた金額が、ワーカーさまの受取金額となります その他ご質問等ありましたら、気軽にお問い合わせください。 ご応募をお待ちしております! |
| https://find.kumoriba.co.jp/amp/s/s.shokunavi-ranpo.jp/tokyo/B2401/B240305/24085917/top_amp/%3Fusqp%3Dxr482KZTMBHZBafV9N3q9-vY6RHxBTB%253D | ||
この度は有難うございます。また細かな修正も早急に対応してくださりありがたかったです。お陰で妥協なくイメージしたデザインに仕上がりました。スキルも高く誠意も伝わりとても感謝致します。また機会がございましたら宜しくお願い致します。
この度は皆様素敵なデザインをありがとうございました!皆様の素敵なデザインに感動し感謝の気持ちでいっぱいでした。コロナ渦で皆様も大変な状況だと思いますが、私も頑張ろうという気持ちになりました。心からありがとうございました。

```html
<!DOCTYPE html>
<html lang="ja">
<head>
<meta charset="utf-8">
<title>Take Out Menu — Trattoria Velare</title>
<link href="https://fonts.googleapis.com/css2?family=Dancing+Script:wght@600;700&family=Playfair+Display:ital,wght@0,600;1,600&family=Zen+Maru+Gothic:wght@500;700&display=swap" rel="stylesheet">
<style>
  :root{
    --green:#1f4a2c;
    --paper:#f6f1e4;
    --ink:#3a2a1e;
    --brown:#5a3d28;
    --muted:#8c7a66;
    --leader:#b5a792;
    --red:#c4332b;
    --white:#fffdf7;
    --illus-warm:#e7d6b4;
    --illus-green:#cfd9bd;
  }
  *{margin:0;padding:0;box-sizing:border-box}
  html,body{width:848px;height:1200px;overflow:hidden;background:var(--paper)}
  body{font-family:"Zen Maru Gothic",sans-serif;color:var(--ink);position:relative}

  .masthead{position:absolute;left:0;top:0;width:848px;height:165px;background:var(--green);color:var(--white);text-align:center}
  .masthead__title{font-family:"Dancing Script",cursive;font-weight:700;font-size:76px;line-height:1;padding-top:26px;letter-spacing:1px}
  .masthead__lead{font-size:17px;letter-spacing:3px;margin-top:12px}
  .masthead__deco{position:absolute;top:30px;width:110px;height:100px;border-radius:12px;background:rgba(255,255,255,.08)}
  .masthead__deco--left{left:30px}
  .masthead__deco--right{right:30px}
  .flag{position:absolute;left:0;top:165px;display:flex;height:10px}
  .flag span{width:52px}
  .flag .g{background:#2f8a45}.flag .w{background:var(--white)}.flag .r{background:var(--red)}

  .column{position:absolute;top:222px}
  .column--left{left:56px;width:352px}
  .column--right{left:458px;width:334px}

  .section{position:relative;margin-bottom:44px}
  .section__head{display:flex;align-items:flex-end;gap:10px;height:46px;margin-bottom:10px}
  .section__title{font-family:"Playfair Display",serif;font-style:italic;font-weight:600;font-size:34px;color:var(--brown);line-height:1}
  .section__note{font-size:11px;color:var(--muted);padding-bottom:6px}
  .section__illus{position:absolute;right:0;top:-8px;height:56px;border-radius:10px}

  .item{display:flex;align-items:flex-end;font-size:15px;font-weight:500;line-height:1.35;padding:7px 0}
  .item__name{flex:0 1 auto}
  .item__name small{font-size:10px}
  .item__leader{flex:1 1 auto;border-bottom:2px dotted var(--leader);margin:0 8px 5px;min-width:20px}
  .item__price{flex:0 0 auto;font-weight:700}

  .illus{position:absolute;border-radius:14px}
  .illus--food{left:470px;top:850px;width:340px;height:110px;background:linear-gradient(180deg,var(--illus-warm),#efe3c8)}
  .illus--chef{left:452px;top:975px;width:80px;height:150px;background:var(--illus-warm)}
  .illus--wine{left:762px;top:975px;width:54px;height:140px;background:#d8c2a8}

  .reserve{position:absolute;left:552px;top:980px;width:128px;height:56px;border:2px solid var(--brown);border-radius:6px;background:var(--white);font-size:12px;font-weight:700;text-align:center;line-height:1.45;padding-top:8px;color:var(--brown)}
  .shop{position:absolute;left:540px;top:1052px;width:214px;text-align:center;color:var(--brown);font-family:"Playfair Display",serif;font-weight:600}
  .shop__kind{font-size:13px;letter-spacing:4px}
  .shop__name{font-size:40px;letter-spacing:3px;line-height:1.05}
  .shop__tel{font-size:24px;letter-spacing:1px;margin-top:4px}

  .footband{position:absolute;left:0;bottom:0;width:848px;height:18px;background:var(--green)}
</style>
</head>
<body>
  <header class="masthead">
    <div class="masthead__deco masthead__deco--left" role="img" aria-label="カトラリーのイラスト"></div>
    <div class="masthead__deco masthead__deco--right" role="img" aria-label="葉っぱのイラスト"></div>
    <h1 class="masthead__title">Take Out Menu</h1>
    <p class="masthead__lead">当店のお料理をお持ち帰りいただけます</p>
  </header>
  <div class="flag"><span class="g"></span><span class="w"></span><span class="r"></span></div>

  <main>
    <div class="column column--left">
      <section class="section">
        <div class="section__head"><h2 class="section__title">Antipasto</h2></div>
        <div class="section__illus" role="img" aria-label="前菜の盛り合わせのイラスト" style="width:120px;background:var(--illus-warm)"></div>
        <div class="item"><span class="item__name">アンチョビポテト</span><span class="item__leader"></span><span class="item__price">¥500</span></div>
        <div class="item"><span class="item__name">ゴルゴンゾーラのキッシュ<small>（2ピース）</small></span><span class="item__leader"></span><span class="item__price">¥600</span></div>
        <div class="item"><span class="item__name">ピクルス＆オリーブ</span><span class="item__leader"></span><span class="item__price">¥500</span></div>
        <div class="item"><span class="item__name">合鴨のロースト</span><span class="item__leader"></span><span class="item__price">¥900</span></div>
        <div class="item"><span class="item__name">いいだこのトマト煮</span><span class="item__leader"></span><span class="item__price">¥950</span></div>
        <div class="item"><span class="item__name">ローストビーフ</span><span class="item__leader"></span><span class="item__price">¥1,200</span></div>
        <div class="item"><span class="item__name">ローストポーク</span><span class="item__leader"></span><span class="item__price">¥900</span></div>
      </section>

      <section class="section">
        <div class="section__head"><h2 class="section__title">Pasta</h2><span class="section__note">※麺は全てリングイネです</span></div>
        <div class="section__illus" role="img" aria-label="パスタのイラスト" style="width:80px;background:var(--illus-warm)"></div>
        <div class="item"><span class="item__name">はまぐりと大粒あさりの<br>ボンゴレビアンコ</span><span class="item__leader"></span><span class="item__price">¥1,500</span></div>
        <div class="item"><span class="item__name">わたりがにのトマトクリーム</span><span class="item__leader"></span><span class="item__price">¥1,500</span></div>
        <div class="item"><span class="item__name">にんにくとアンチョビの<br>ペペロンチーノ</span><span class="item__leader"></span><span class="item__price">¥900</span></div>
        <div class="item"><span class="item__name">ゴルゴンゾーラのペンネ</span><span class="item__leader"></span><span class="item__price">¥1,300</span></div>
        <div class="item"><span class="item__name">アラビアータのペンネ</span><span class="item__leader"></span><span class="item__price">¥900</span></div>
      </section>

      <section class="section">
        <div class="section__head"><h2 class="section__title">Specialita</h2></div>
        <div class="section__illus" role="img" aria-label="アヒージョのスキレットのイラスト" style="width:130px;background:var(--illus-warm)"></div>
        <div class="item"><span class="item__name">天使の海老のクリーム煮</span><span class="item__leader"></span><span class="item__price">¥700</span></div>
        <div class="item"><span class="item__name">つぶ貝と小海老の<br>エスカルゴバター</span><span class="item__leader"></span><span class="item__price">¥800</span></div>
        <div class="item"><span class="item__name">魚介の旨み凝縮アヒージョ</span><span class="item__leader"></span><span class="item__price">¥900</span></div>
        <div class="item"><span class="item__name">ラザニア</span><span class="item__leader"></span><span class="item__price">¥1,000</span></div>
        <div class="item"><span class="item__name">バケット<small>（2ピース）</small></span><span class="item__leader"></span><span class="item__price">¥300</span></div>
      </section>
    </div>

    <div class="column column--right">
      <section class="section">
        <div class="section__head"><h2 class="section__title">Pizza</h2></div>
        <div class="section__illus" role="img" aria-label="ピザとワインのイラスト" style="width:96px;background:var(--illus-warm)"></div>
        <div class="item"><span class="item__name">マルゲリータ</span><span class="item__leader"></span><span class="item__price">¥1,500</span></div>
        <div class="item"><span class="item__name">クアトロフォルマッジョ</span><span class="item__leader"></span><span class="item__price">¥1,700</span></div>
        <div class="item"><span class="item__name">博多明太子のクリームピザ</span><span class="item__leader"></span><span class="item__price">¥1,600</span></div>
        <div class="item"><span class="item__name">ザ・サルシッチャ</span><span class="item__leader"></span><span class="item__price">¥1,600</span></div>
      </section>

      <section class="section">
        <div class="section__head"><h2 class="section__title">Insalata</h2><span class="section__note">※2〜3人前</span></div>
        <div class="section__illus" role="img" aria-label="サラダのイラスト" style="width:84px;background:var(--illus-green)"></div>
        <div class="item"><span class="item__name">生ハムのグリーンサラダ</span><span class="item__leader"></span><span class="item__price">¥1,000</span></div>
        <div class="item"><span class="item__name">イタリアンゴボウとフレンチサラダ</span><span class="item__leader"></span><span class="item__price">¥1,000</span></div>
        <div class="item"><span class="item__name">VELAREのシーザーサラダ</span><span class="item__leader"></span><span class="item__price">¥1,000</span></div>
        <div class="item"><span class="item__name">フレンチサラダS</span><span class="item__leader"></span><span class="item__price">¥450</span></div>
      </section>

      <section class="section">
        <div class="section__head"><h2 class="section__title">Dolce</h2></div>
        <div class="section__illus" role="img" aria-label="ケーキのイラスト" style="width:70px;background:var(--illus-warm)"></div>
        <div class="item"><span class="item__name">ガトーショコラ</span><span class="item__leader"></span><span class="item__price">¥500</span></div>
        <div class="item"><span class="item__name">ティラミス</span><span class="item__leader"></span><span class="item__price">¥500</span></div>
      </section>
    </div>
  </main>

  <div class="illus illus--food" role="img" aria-label="パンと野菜と食材のイラスト"></div>
  <div class="illus illus--chef" role="img" aria-label="コックのイラスト"></div>
  <div class="illus illus--wine" role="img" aria-label="ワインボトルとグラスのイラスト"></div>

  <div class="reserve">事前の予約を<br>お願いいたします</div>

  <div class="shop">
    <div class="shop__kind">TRATTORIA</div>
    <div class="shop__name">VELARE</div>
    <div class="shop__tel">03-4827-5190</div>
  </div>

  <div class="footband"></div>
</body>
</html>
```